VEK.PRO- Daniel Whitcombe Fitness- needs a clever business card using the logo, name, info, contact

I need a business card designed for my Online Personal Training company called VEK.PRO, abbreviation for Daniel Whitcombe Fitness. My company focuses on coaching in personal health and personal growth to unleash your greatest potential. I would like to see designs that use my color scheme of a redish-orange (C:0,M:84,Y:100,K:0), grey, white, black, and my company font is OSWALD. The final design should communicate some aspects of design, health, motivation, growth, in some way. The logo is very important to the company and can be displayed in any of the colors previously mentioned. Must include the company name, my website: www.vek.example , my email: dan@vek.example

Target Market(s)

Personal health, fitness, general public, those who lack knowledge, awareness, and confidence in personal health

Industry/Entity Type

Personal Trainer

Font styles to use
Other font styles liked:
• OSWALD. (Bold, Regular, Light)

Colors
f37122
ffffff
9d9d9d
000000

Requirements
Must have
• Must include the logo, company name, my website: www.vek.example , my email: dan@vek.example
Nice to have
• Variations of the colors scheme of a redish-orange (C:0,M:84,Y:100,K:0), grey, white, black. Logo, card, or text can be in any of these colors.
• Possible quote like "Take control of your personal health to unleash your greatest potential" or "Unleashing your greatness first begins with fitness of the body and mind"

```html
<!DOCTYPE html>
<html lang="en">
<head>
<meta charset="utf-8">
<title>VEK.PRO Business Card</title>
<link rel="stylesheet" href="https://fonts.googleapis.com/css2?family=Oswald:wght@300;400;700&family=Open+Sans:wght@400;600&display=swap">
<style>
  :root {
    --brand-orange: #f05322;
    --card-frost: #ecebea;
    --ink: #1d1d1d;
    --white: #ffffff;
    --page-bg: #d9d9d9;
  }
  html, body {
    margin: 0;
    width: 1200px;
    height: 900px;
    overflow: hidden;
    background: var(--page-bg);
  }
  .business-card {
    position: absolute;
    left: 150px;
    top: 171px;
    width: 670px;
    height: 415px;
    transform: scale(1.343);
    transform-origin: top left;
  }
  .card-shape {
    position: absolute;
    inset: 0;
    width: 670px;
    height: 415px;
  }
  .holder-name {
    position: absolute;
    left: 32px;
    top: 34px;
    margin: 0;
    font: 400 25px/1 "Open Sans", sans-serif;
    color: var(--white);
  }
  .holder-title {
    position: absolute;
    left: 32px;
    top: 70px;
    margin: 0;
    font: 400 16px/1 "Open Sans", sans-serif;
    color: var(--white);
  }
  .company-name {
    position: absolute;
    left: 30px;
    top: 150px;
    margin: 0;
    font: 700 64px/1 "Oswald", sans-serif;
    color: var(--ink);
    letter-spacing: 0.5px;
  }
  .company-tagline {
    position: absolute;
    left: 32px;
    top: 230px;
    margin: 0;
    font: 300 19px/1 "Oswald", sans-serif;
    color: var(--ink);
    text-transform: uppercase;
  }
  .contact-list {
    position: absolute;
    left: 32px;
    top: 317px;
    margin: 0;
    padding: 0;
    list-style: none;
    font: 400 16px/24.5px "Open Sans", sans-serif;
    color: var(--white);
  }
  .contact-list li {
    display: flex;
    align-items: center;
    gap: 9px;
  }
  .contact-icon {
    width: 14px;
    height: 14px;
    fill: var(--white);
  }
  .logo-name {
    position: absolute;
    left: 267px;
    top: 172px;
    width: 400px;
    margin: 0;
    text-align: center;
    font: 700 58px/1 "Oswald", sans-serif;
    color: var(--brand-orange);
  }
</style>
</head>
<body>
  <article class="business-card">
    <svg class="card-shape" viewBox="0 0 670 415" aria-hidden="true">
      <path d="M0 0 H462 A207.5 207.5 0 0 1 462 415 H0 Z" fill="var(--brand-orange)"/>
      <rect x="0" y="117" width="320" height="178" fill="var(--card-frost)"/>
      <circle cx="462" cy="207.5" r="195" fill="var(--card-frost)"/>
    </svg>

    <h2 class="holder-name">Aaron Mercer</h2>
    <p class="holder-title">Managing Director</p>

    <h1 class="company-name">VEK.PRO</h1>
    <p class="company-tagline">Daniel Whitcombe Fitness</p>

    <ul class="contact-list">
      <li>
        <svg class="contact-icon" viewBox="0 0 24 24"><path d="M6.6 10.8a15.1 15.1 0 0 0 6.6 6.6l2.2-2.2c.3-.3.7-.4 1-.2 1.1.4 2.3.6 3.6.6.6 0 1 .4 1 1V20c0 .6-.4 1-1 1A17 17 0 0 1 3 4c0-.6.4-1 1-1h3.5c.6 0 1 .4 1 1 0 1.3.2 2.5.6 3.6.1.3 0 .7-.2 1z"/></svg>
        <span>044-555 010 203</span>
      </li>
      <li>
        <svg class="contact-icon" viewBox="0 0 24 24"><path d="M2 5h20v14H2z M3.5 6.5 12 13l8.5-6.5" fill="var(--white)" stroke="var(--brand-orange)" stroke-width="1.6"/></svg>
        <span>dan@vek.example</span>
      </li>
      <li>
        <svg class="contact-icon" viewBox="0 0 24 24"><path d="M10 14a4 4 0 0 1 0-5.6l3-3a4 4 0 0 1 5.6 5.6l-1.5 1.5M14 10a4 4 0 0 1 0 5.6l-3 3a4 4 0 0 1-5.6-5.6l1.5-1.5" fill="none" stroke="var(--white)" stroke-width="2.4" stroke-linecap="round"/></svg>
        <span>www.vek.example</span>
      </li>
    </ul>

    <p class="logo-name">VEK.PRO</p>
  </article>
</body>
</html>
```